Editorial Website Design for High-End Custom Millwork Firm

Design (no development) for a 5-7 page website for a high-end custom architectural millwork firm. Editorial, magazine-quality aesthetic — think Interior Almanac and top-tier millwork studios (Elwin Strade, Korvo). Full brief, reference sites, and project photography attached. We have uploaded a sample of our photography to use in your design. PLEASE READ PDF DOCUMENT BRIEF!!!

1 page

```html
<!DOCTYPE html>
<html lang="en">
<head>
<meta charset="utf-8">
<title>Halvorn &amp; Vale — Architectural Woodwork</title>
<link rel="stylesheet" href="https://fonts.googleapis.com/css2?family=Libre+Caslon+Text:wght@400;700&family=Inter:wght@400;500;600&display=swap">
<style>
:root{
  --cream:#f4f0e9;
  --sand:#e9e2d7;
  --band:#e3dbcf;
  --brown:#7a5a42;
  --brown-dark:#5e4431;
  --ink:#2b241e;
  --muted:#7c7268;
  --line:#cfc4b5;
  --white:#ffffff;
  --serif:"Libre Caslon Text", Georgia, serif;
  --sans:"Inter", Arial, sans-serif;
}
*{box-sizing:border-box;margin:0;padding:0}
html,body{width:1200px;height:4409px;overflow:hidden;background:var(--white)}
body{position:relative;font-family:var(--sans);color:var(--ink)}
.desktop{position:absolute;left:115px;top:63px;width:1440px;height:7545px;transform:scale(.4993);transform-origin:0 0;background:var(--cream);overflow:hidden}
.mobile{position:absolute;left:909px;top:63px;width:390px;height:9540px;transform:scale(.45);transform-origin:0 0;background:var(--cream);overflow:hidden;border-radius:46px;border:3px solid #d9d3ca}
.abs{position:absolute}
.photo{border-radius:6px}
.serif{font-family:var(--serif);font-weight:400;letter-spacing:-.01em}
.eyebrow{font-size:12px;letter-spacing:.08em;text-transform:uppercase;color:var(--muted);font-weight:500}
.para{font-size:14px;line-height:1.6;color:var(--muted)}
.btn{display:inline-block;background:var(--brown);color:var(--white);font-size:14px;font-weight:500;padding:11px 22px;border-radius:3px}
.btn-ghost{display:inline-block;border:1px solid var(--brown);color:var(--brown);font-size:14px;padding:10px 20px;border-radius:3px;background:var(--cream)}
.link{font-size:12px;font-weight:600;color:var(--ink)}
.icon-box{width:40px;height:40px;background:var(--brown);border-radius:3px;display:flex;align-items:center;justify-content:center}
.social{width:40px;height:40px;background:#3a2e25;border-radius:6px}
.wordmark{font-family:var(--sans);font-weight:500;font-size:22px;color:var(--ink);display:flex;align-items:center;gap:10px}
.wordmark .mark{width:14px;height:14px;background:var(--brown);display:inline-block}
.nav-links{display:flex;gap:32px;font-size:14px;color:var(--ink);align-items:center}
.svc{background:var(--sand);border-radius:4px;padding:34px 34px}
.svc h3{font-size:19px;font-weight:500;margin:24px 0 14px}
.svc p{font-size:13px;line-height:1.6;color:var(--muted);margin-bottom:14px}
.tile{border-radius:4px;padding:24px;color:var(--white)}
.tile h4{font-size:17px;font-weight:500;margin:12px 0 6px}
.tile p{font-size:12px;line-height:1.5;opacity:.85}
.quote{background:var(--white);border:1px solid var(--line);border-radius:4px;padding:30px}
.stars{color:#b8895c;font-size:18px;letter-spacing:4px}
.article{background:var(--white);border-radius:4px;overflow:hidden;box-shadow:0 2px 10px rgba(0,0,0,.06)}
.article h4{font-family:var(--serif);font-weight:400;font-size:16px;line-height:1.3;margin:18px 18px 10px}
.article p{font-size:12px;line-height:1.55;color:var(--muted);margin:0 18px 14px}
.article .link{margin:0 18px}
.foot-col h5{font-size:16px;font-weight:600;color:var(--white);margin-bottom:14px}
.foot-col li{list-style:none;font-size:12px;color:#efe4d6;line-height:1.9}
.center{text-align:center}
</style>
</head>
<body>

<main class="desktop">

  <header class="abs" style="left:62px;top:26px;right:55px;display:flex;justify-content:space-between;align-items:center">
    <div class="wordmark"><span class="mark"></span>Halvorn &amp; Vale</div>
    <nav class="nav-links"><span>Home</span><span>Projects</span><span>Services</span><span>About</span><span>Journal</span><span>Contact</span><span class="btn" style="padding:10px 20px">Start a Project</span></nav>
  </header>

  <section class="abs photo" style="left:55px;top:100px;width:1330px;height:703px;background:linear-gradient(90deg,#f3efe8 0%,#ece6dc 35%,#c9b9a3 55%,#9a7a57 75%,#6d6a62 100%)" role="img" aria-label="Double-height interior with a slatted wood feature wall, steel stair and living plant wall">
    <div class="abs" style="left:65px;top:118px;width:560px">
      <div class="eyebrow" style="font-size:11px">Serving commercial &amp; residential clients throughout the Southeast</div>
      <h1 class="serif" style="font-size:56px;line-height:1.38;margin:14px 0 18px">Architectural Millwork Crafted Without Compromise</h1>
      <p class="para" style="font-size:13px;width:420px">For more than three decades, Halvorn &amp; Vale has partnered with architects, designers, builders, and homeowners to create exceptional commercial interiors and bespoke residential spaces, crafted to the highest standards.</p>
      <div style="margin-top:28px;display:flex;gap:16px"><span class="btn">Start a Project</span><span class="btn-ghost">Our Capabilities</span></div>
    </div>
    <div class="abs" style="right:34px;top:455px;display:flex;flex-direction:column;gap:38px">
      <div class="social"></div><div class="social"></div><div class="social"></div>
    </div>
  </section>

  <section class="abs" style="left:55px;top:900px;width:1330px;height:300px">
    <div class="abs" style="left:0;top:0;width:520px">
      <div class="eyebrow" style="font-size:11px">About Halvorn &amp; Vale</div>
      <h2 class="serif" style="font-size:50px;line-height:1.4;margin-top:10px">Craftsmanship Built Around Every Detail.</h2>
    </div>
    <div class="abs" style="left:566px;top:12px;width:1px;height:272px;background:var(--brown)"></div>
    <div class="abs" style="left:661px;top:8px;width:668px">
      <p class="para" style="font-size:13.5px">Since 1988, Halvorn &amp; Vale has earned a reputation for producing architectural millwork that meets the highest standards of quality, precision, and durability. Every project is designed, engineered, fabricated, and finished within our Linden Falls facility, allowing complete control from concept through installation.</p>
      <p class="para" style="font-size:13.5px">Our firm was established in 1988 and is located in historic Linden Falls, North Carolina. We are a Minority Owned Business Enterprise with a long tradition of employee participation. We draw on this area's history of fine furniture making and have attracted skilled craftsmen and finish people from all over the country. With an average of twelve years employment, our team helps us not only grow but elevate the quality and complexity of work as well.</p>
      <span class="btn-ghost" style="margin-top:22px;font-size:12px;padding:8px 18px">Learn Our Story →</span>
    </div>
  </section>

  <div class="abs photo" style="left:55px;top:1245px;width:1330px;height:497px;background:linear-gradient(120deg,#8a7560,#c8b9a3 40%,#6f6354 70%,#a89680)" role="img" aria-label="Two craftsmen reviewing drawings at a workbench in the shop"></div>

  <section class="abs" style="left:55px;top:1742px;width:1330px;height:978px">
    <div class="center" style="margin-top:108px">
      <div class="eyebrow" style="font-size:11px">Our Services</div>
      <h2 class="serif" style="font-size:46px;margin:12px 0 16px">From Design Intent To Final Installation</h2>
      <p class="para" style="width:760px;margin:0 auto;font-size:13px">Whether fabricating custom reception desks, luxury hotel millwork, executive boardrooms, university interiors, or bespoke residential cabinetry, our experienced team delivers exceptional craftsmanship throughout every phase of production.</p>
    </div>
    <div style="display:grid;grid-template-columns:repeat(3,1fr);gap:26px 27px;margin-top:76px">
      <div class="svc" style="height:240px"><div class="icon-box"><svg width="20" height="20" viewBox="0 0 20 20" fill="none" stroke="#fff" stroke-width="1.5"><rect x="3" y="3" width="14" height="14"/><path d="M3 10h14M10 3v14"/></svg></div><h3>Custom Architectural Millwork</h3><p>Lorem ipsum dolor sit amet, consectetur adipiscing elit, sed do eiusmod tempor incididunt ut labore et dolore magna aliqua. Ut enim ad minim veniam.</p><span class="link">Learn Our Story →</span></div>
      <div class="svc" style="height:240px"><div class="icon-box"><svg width="20" height="20" viewBox="0 0 20 20" fill="none" stroke="#fff" stroke-width="1.5"><rect x="4" y="2" width="12" height="16"/><path d="M7 6h6M7 10h6M7 14h6"/></svg></div><h3>Commercial Interiors</h3><p>Lorem ipsum dolor sit amet, consectetur adipiscing elit, sed do eiusmod tempor incididunt ut labore et dolore magna aliqua. Ut enim ad minim veniam.</p><span class="link">Learn Our Story →</span></div>
      <div class="svc" style="height:240px"><div class="icon-box"><svg width="20" height="20" viewBox="0 0 20 20" fill="none" stroke="#fff" stroke-width="1.5"><rect x="4" y="2" width="12" height="16"/><path d="M10 6v8"/></svg></div><h3>Luxury Residential Cabinetry</h3><p>Lorem ipsum dolor sit amet, consectetur adipiscing elit, sed do eiusmod tempor incididunt ut labore et dolore magna aliqua. Ut enim ad minim veniam.</p><span class="link">Learn Our Story →</span></div>
      <div class="svc" style="height:240px"><div class="icon-box"><svg width="20" height="20" viewBox="0 0 20 20" fill="none" stroke="#fff" stroke-width="1.5"><path d="M3 9l7-6 7 6v8H3z"/><path d="M8 17v-5h4v5"/></svg></div><h3>Conference Rooms</h3><p>Lorem ipsum dolor sit amet, consectetur adipiscing elit, sed do eiusmod tempor incididunt ut labore et dolore magna aliqua. Ut enim ad minim veniam.</p><span class="link">Learn Our Story →</span></div>
      <div class="svc" style="height:240px"><div class="icon-box"><svg width="20" height="20" viewBox="0 0 20 20" fill="none" stroke="#fff" stroke-width="1.5"><path d="M3 5h14v4H3zM5 9v8h10V9"/></svg></div><h3>Educational Facilities</h3><p>Lorem ipsum dolor sit amet, consectetur adipiscing elit, sed do eiusmod tempor incididunt ut labore et dolore magna aliqua. Ut enim ad minim veniam.</p><span class="link">Learn Our Story →</span></div>
      <div class="svc" style="height:240px"><div class="icon-box"><svg width="20" height="20" viewBox="0 0 20 20" fill="none" stroke="#fff" stroke-width="1.5"><rect x="3" y="3" width="14" height="14"/><path d="M3 8h14M3 13h14"/></svg></div><h3>Retail Fixtures</h3><p>Lorem ipsum dolor sit amet, consectetur adipiscing elit, sed do eiusmod tempor incididunt ut labore et dolore magna aliqua. Ut enim ad minim veniam.</p><span class="link">Learn Our Story →</span></div>
    </div>
    <div class="center" style="margin-top:36px"><span class="btn">Explore Capabilities</span></div>
  </section>

  <section class="abs" style="left:55px;top:2720px;width:1330px;height:535px">
    <div class="abs" style="left:0;top:120px;width:520px">
      <div class="eyebrow" style="font-size:11px">Why Choose Us</div>
      <h2 class="serif" style="font-size:46px;line-height:1.4;margin:8px 0 14px">Built To The Highest Industry Standards</h2>
      <p class="para" style="font-size:13px">Whether fabricating custom reception desks, luxury hotel millwork, executive boardrooms, university interiors, or bespoke residential cabinetry, our experienced team delivers exceptional craftsmanship throughout every phase of production.</p>
      <span class="btn" style="margin-top:24px">Explore Capabilities</span>
    </div>
    <div class="abs tile" style="left:627px;top:10px;width:322px;height:205px;background:#d8cfc2;color:var(--ink)"><svg width="26" height="26" viewBox="0 0 26 26" fill="none" stroke="#5e4431" stroke-width="1.5"><circle cx="13" cy="13" r="9"/><path d="M13 8v5l3 3"/></svg><h4>36+ Years</h4><p>Trusted craftsmanship since 1988.</p><p class="link" style="margin-top:14px">Learn Our Story →</p></div>
    <div class="abs tile" style="left:964px;top:0;width:366px;height:230px;background:linear-gradient(135deg,#4b4540,#7a7064)" role="img" aria-label="Finisher spraying a cabinet panel"><h4 style="margin-top:64px">Premium Grade</h4><p>Certified to premium grade standards with rigorous quality checks on every piece.</p><p class="link" style="color:#fff;margin-top:12px">Learn Our Story →</p></div>
    <div class="abs tile" style="left:614px;top:247px;width:362px;height:233px;background:linear-gradient(135deg,#3f3a35,#6c6459)" role="img" aria-label="Fabrication floor with machinery"><h4 style="margin-top:96px">Complete Manufacturing</h4><p>Engineering, fabrication, finishing, and installation under one roof.</p><p class="link" style="color:#fff;margin-top:12px">Learn Our Story →</p></div>
    <div class="abs tile" style="left:990px;top:275px;width:326px;height:195px;background:var(--brown)"><svg width="26" height="26" viewBox="0 0 26 26" fill="none" stroke="#fff" stroke-width="1.5"><circle cx="13" cy="10" r="6"/><path d="M9 15l-2 8 6-3 6 3-2-8"/></svg><h4>Award Quality</h4><p>Recognized for exceptional precision and enduring craftsmanship.</p><p class="link" style="color:#fff;margin-top:12px">Learn Our Story →</p></div>
  </section>

  <section class="abs" style="left:0;top:3255px;width:1440px;height:900px;background:var(--band)">
    <div class="center" style="margin-top:98px">
      <div class="eyebrow" style="font-size:11px">Our Portfolio</div>
      <h2 class="serif" style="font-size:46px;margin:10px 0 14px">Showcasing Our Work</h2>
      <p class="para" style="width:700px;margin:0 auto;font-size:13px">Explore a selection of custom millwork and cabinetry projects crafted with precision, blending timeless design, exceptional craftsmanship, and lasting durability across commercial and residential environments.</p>
    </div>
    <div class="abs photo" style="left:55px;top:263px;width:415px;height:505px;background:linear-gradient(180deg,#2f2b28,#4a4540 55%,#6c6863)" role="img" aria-label="Executive boardroom with a long conference table and dark chairs">
      <div class="abs" style="left:24px;top:24px;display:flex;gap:8px;align-items:center;color:#fff;font-size:12px"><svg width="12" height="14" viewBox="0 0 12 14" fill="#fff"><path d="M6 0a5 5 0 0 0-5 5c0 4 5 9 5 9s5-5 5-9a5 5 0 0 0-5-5zm0 7a2 2 0 1 1 0-4 2 2 0 0 1 0 4z"/></svg>Linden Falls, North Carolina</div>
      <div class="abs" style="right:20px;top:16px;width:48px;height:48px;border:1.5px solid #fff;border-radius:50%;display:flex;align-items:center;justify-content:center"><svg width="18" height="18" viewBox="0 0 18 18" fill="none" stroke="#fff" stroke-width="1.6"><path d="M4 14L14 4M6 4h8v8"/></svg></div>
      <div class="abs serif" style="left:28px;bottom:64px;color:#fff;font-size:22px">Executive Office Headquarters</div>
      <div class="abs" style="left:28px;bottom:42px;color:#ddd;font-size:12px">Corporate</div>
    </div>
    <div class="abs photo" style="left:511px;top:263px;width:418px;height:505px;background:linear-gradient(180deg,#6d86a0,#9bb0c2 50%,#c9b89e)" role="img" aria-label="Blue painted kitchen cabinetry with brass fixtures"></div>
    <div class="abs photo" style="left:970px;top:263px;width:415px;height:505px;background:linear-gradient(180deg,#6b4a2c,#b37a3e 45%,#9a3f23)" role="img" aria-label="Warm lounge with rust sofas and ornate wood ceiling"></div>
    <div class="abs center" style="left:0;right:0;top:808px"><span class="btn">View Full Portfolio</span></div>
  </section>

  <section class="abs" style="left:0;top:4245px;width:1440px;height:470px">
    <div class="abs" style="left:0;top:0;width:720px;height:470px;background:linear-gradient(120deg,#7a6a4e,#c69a6a 40%,#4b6a5a 75%,#b38860)" role="img" aria-label="Hospitality lounge with globe pendants and colorful seating"></div>
    <div class="abs" style="left:720px;top:0;width:720px;height:470px;background:linear-gradient(120deg,#c6b29a,#a88c70 45%,#d9cdbd)" role="img" aria-label="Light oak cabinetry wall in a wellness interior"></div>
    <div class="abs center" style="left:110px;top:150px;width:500px;height:160px;background:rgba(110,82,60,.82);border-radius:4px;color:#fff;padding:26px 34px;font-size:13px;line-height:1.55">From hospitality and higher education to corporate headquarters and luxury retail environments, Halvorn &amp; Vale delivers architectural millwork that meets the demanding standards of architects and contractors.<div style="font-weight:600;margin-top:14px">Commercial Projects →</div></div>
    <div class="abs center" style="left:850px;top:170px;width:460px;height:130px;background:rgba(110,82,60,.82);border-radius:4px;color:#fff;padding:26px 34px;font-size:13px;line-height:1.55">Thoughtfully crafted cabinetry and built-ins that bring timeless design and exceptional craftsmanship into private homes.<div style="font-weight:600;margin-top:14px">Residential Projects →</div></div>
  </section>

  <section class="abs" style="left:55px;top:4812px;width:1330px;height:580px">
    <div class="abs photo" style="left:0;top:0;width:542px;height:580px;background:linear-gradient(140deg,#6e6a66,#b3a48d 45%,#e3ddd3 70%,#8a7a66)" role="img" aria-label="Craftsman assembling a white lattice screen panel in the shop"></div>
    <div class="abs" style="left:567px;top:0;width:763px">
      <div class="eyebrow" style="font-size:11px">Client Testimonials</div>
      <h2 class="serif" style="font-size:46px;line-height:1.38;margin:8px 0 14px">Trusted By Architects, Builders &amp; Designers</h2>
      <p class="para" style="font-size:13px">For more than three decades, Halvorn &amp; Vale has partnered with leading architects, contractors, designers, and developers to deliver custom architectural millwork with precision, craftsmanship, and reliability.</p>
    </div>
    <div class="abs quote" style="left:567px;top:262px;width:380px;height:318px">
      <div class="stars">★★★★★</div>
      <p class="para" style="font-size:12.5px;margin-top:14px">"Halvorn &amp; Vale helped me by designing not only a beautiful, but a very functional kitchen and dining space. We were pleased with all the steps of the process, from design to installation. They paid great attention to detail and the results were amazing."</p>
      <div class="abs" style="left:30px;bottom:28px;display:flex;gap:12px;align-items:center"><div style="width:44px;height:44px;border-radius:50%;background:#b7a895" role="img" aria-label="Client portrait"></div><div><div style="font-size:13px;font-weight:600">Dana Merrow</div><div style="font-size:11px;color:var(--muted)">CEO, company</div></div></div>
      <div class="abs serif" style="right:30px;bottom:12px;font-size:60px;color:#c8bcad">”</div>
    </div>
    <div class="abs quote" style="left:965px;top:262px;width:365px;height:318px">
      <div class="stars">★★★★★</div>
      <p class="para" style="font-size:12.5px;margin-top:14px">"Halvorn &amp; Vale consistently delivers exceptional craftsmanship with unmatched attention to detail. Their team understands the importance of precision, communicates clearly throughout every phase, and always exceeds our expectations."</p>
      <div class="abs" style="left:30px;bottom:28px;display:flex;gap:12px;align-items:center"><div style="width:44px;height:44px;border-radius:50%;background:#b7a895" role="img" aria-label="Client portrait"></div><div><div style="font-size:13px;font-weight:600">Dana Merrow</div><div style="font-size:11px;color:var(--muted)">CEO, company</div></div></div>
      <div class="abs serif" style="right:30px;bottom:12px;font-size:60px;color:#c8bcad">”</div>
    </div>
    <svg class="abs" style="left:1345px;top:278px" width="14" height="22" viewBox="0 0 14 22" fill="none" stroke="#2b241e" stroke-width="1.6"><path d="M3 3l8 8-8 8"/></svg>
  </section>

  <section class="abs" style="left:55px;top:5497px;width:1330px;height:463px;background:var(--sand);border-radius:4px">
    <div class="abs photo" style="left:0;top:0;width:450px;height:463px;background:linear-gradient(150deg,#3d342c,#7a6047 45%,#c2a37f 75%,#5c4a3a)" role="img" aria-label="Coffered wood ceiling over an open office interior"></div>
    <div class="abs" style="left:545px;top:40px;width:700px">
      <div class="eyebrow" style="font-size:11px">Client Testimonials</div>
      <h2 class="serif" style="font-size:46px;line-height:1.4;margin:8px 0 14px">Let's Build Something Exceptional.</h2>
      <p class="para" style="font-size:13px;width:560px">Whether you're planning a commercial interior or a custom residential project, we'd welcome the opportunity to collaborate.</p>
      <div style="display:flex;gap:16px;margin-top:40px"><div style="width:350px;height:44px;background:var(--white);border:1px solid var(--line);border-radius:3px;font-size:12px;color:var(--muted);padding:14px 16px">Email</div><span class="btn" style="padding:13px 34px">Contact Us</span></div>
      <div style="display:flex;gap:22px;margin-top:28px;align-items:center"><div style="width:52px;height:52px;border-radius:50%;background:#3e4f7a"></div><div style="width:64px;height:52px;border-radius:3px;background:#9c8a4a"></div><div style="width:52px;height:52px;border-radius:50%;background:#4f5f3c"></div></div>
    </div>
  </section>

  <section class="abs" style="left:55px;top:6064px;width:1330px;height:700px">
    <div class="center" style="margin-top:44px">
      <div class="eyebrow" style="font-size:11px">Latest Insights</div>
      <h2 class="serif" style="font-size:46px;margin:10px 0 14px">Insights &amp; Recent Projects</h2>
      <p class="para" style="width:700px;margin:0 auto;font-size:13px">Explore expert perspectives, project highlights, and behind-the-scenes stories showcasing the craftsmanship, innovation, and attention to detail that define every Halvorn &amp; Vale project.</p>
    </div>
    <svg class="abs" style="left:-12px;top:322px" width="14" height="22" viewBox="0 0 14 22" fill="none" stroke="#2b241e" stroke-width="1.6"><path d="M11 3L3 11l8 8"/></svg>
    <svg class="abs" style="right:-12px;top:322px" width="14" height="22" viewBox="0 0 14 22" fill="none" stroke="#2b241e" stroke-width="1.6"><path d="M3 3l8 8-8 8"/></svg>
    <div class="abs" style="left:7px;top:220px;display:grid;grid-template-columns:repeat(4,291px);gap:52px">
      <div class="article" style="height:395px"><div style="height:220px;margin:14px 14px 0;background:linear-gradient(160deg,#e6ddcf,#c7a878 60%,#8d6a48)" role="img" aria-label="Bright kitchen with pendant lights and wood island"></div><h4>5 Architectural Millwork Trends Shaping Modern Commercial Interiors</h4><p>Discover the latest innovations, finishes, and design approaches transforming offices, hospitality spaces, and more.</p><span class="link">Read Article →</span></div>
      <div class="article" style="height:395px"><div style="height:220px;margin:14px 14px 0;background:linear-gradient(160deg,#e4e2de,#7d8fa3 55%,#564b40)" role="img" aria-label="Corporate lobby with a carved reception desk"></div><h4>Crafting a Custom Lobby for a Luxury Corporate Headquarters</h4><p>Take an inside look at how our team transformed a vision into a sophisticated, functional space through precision millwork.</p><span class="link">Read Article →</span></div>
      <div class="article" style="height:395px"><div style="height:220px;margin:14px 14px 0;background:linear-gradient(160deg,#3f342b,#8c6b4a 50%,#c8b093)" role="img" aria-label="Office space under a coffered wood ceiling"></div><h4>From Design to Installation: The Journey of Custom Millwork</h4><p>Follow our process from engineering and fabrication to finishing and on-site installation for every project.</p><span class="link">Read Article →</span></div>
      <div class="article" style="height:395px"><div style="height:220px;margin:14px 14px 0;background:linear-gradient(160deg,#e1b778,#c48a48 55%,#8a5b30)" role="img" aria-label="Library wall of warm maple shelving"></div><h4>Choosing the Right Wood Species for Lasting Architectural Millwork</h4><p>Compare popular hardwoods, veneers, and finishes to find the ideal balance of beauty and durability.</p><span class="link">Read Article →</span></div>
    </div>
    <div class="abs center" style="left:0;right:0;top:652px"><span class="btn">View All Articles</span></div>
  </section>

  <footer class="abs" style="left:0;top:6873px;width:1440px;height:672px;background:linear-gradient(180deg,#8a6849,#93714f 50%,#7b5b3f);color:var(--white)" role="img" aria-label="Footer over a faint workshop shelving backdrop">
    <div class="abs" style="left:62px;top:84px"><div style="font-family:var(--sans);font-weight:500;font-size:42px;display:flex;align-items:center;gap:16px"><span style="width:26px;height:26px;background:#f2ebe2;display:inline-block"></span>Halvorn &amp; Vale</div><div style="font-size:12px;margin-top:10px;opacity:.85">Architectural woodwork and interiors since 1988</div></div>
    <div class="abs" style="right:96px;top:100px;display:flex;gap:28px"><div class="social" style="background:#f2ebe2;width:46px;height:46px"></div><div class="social" style="background:#f2ebe2;width:46px;height:46px"></div><div class="social" style="background:#f2ebe2;width:46px;height:46px"></div></div>
    <div class="abs" style="left:55px;top:285px;display:flex;gap:90px">
      <div class="foot-col"><h5>Company</h5><ul><li>Home</li><li>Projects</li><li>Services</li><li>About</li><li>Journal</li><li>Contact</li></ul></div>
      <div class="foot-col"><h5>Projects</h5><ul><li>Commercial</li><li>Residential</li><li>Hospitality</li><li>Education</li><li>Luxury Homes</li><li>Corporate</li></ul></div>
      <div class="foot-col"><h5>Capabilities</h5><ul><li>Architectural Millwork</li><li>Custom Cabinetry</li><li>Engineering</li><li>Finishing</li><li>Installation</li><li>Contact</li></ul></div>
      <div class="foot-col"><h5>Contact</h5><ul><li style="font-weight:600">Address</li><li>418 Cedar Row</li><li>Linden Falls, NC 27510</li><li style="font-weight:600">Phone</li><li>919-555-0142</li><li style="font-weight:600">Email</li><li>studio@halvornvale.com</li></ul></div>
    </div>
    <div class="abs" style="left:1050px;top:268px;width:335px">
      <div style="font-size:10px;letter-spacing:.1em">NEWSLETTER</div>
      <div style="font-size:22px;font-weight:500;margin:6px 0 16px">Contact Us</div>
      <div style="display:flex;border-bottom:1px solid #e6d8c6;padding-bottom:6px;align-items:center;justify-content:space-between"><span style="font-size:12px;opacity:.85">Enter your email</span><span style="background:#f2ebe2;color:var(--brown);font-size:11px;padding:7px 12px;border-radius:3px">Send Now</span></div>
      <div style="display:flex;gap:24px;margin-top:30px"><div style="width:46px;height:46px;border-radius:50%;background:#3e4f7a"></div><div style="width:56px;height:46px;border-radius:3px;background:#a99850"></div><div style="width:46px;height:46px;border-radius:50%;background:#4f5f3c"></div></div>
    </div>
    <div class="abs" style="left:55px;right:55px;top:580px;display:flex;justify-content:space-between;font-size:12px;opacity:.9"><span>Halvorn &amp; Vale. All Rights Reserved</span><span>Back to top &nbsp;↑</span></div>
  </footer>
</main>

<main class="mobile">
  <header class="abs" style="left:18px;top:44px;right:18px;display:flex;justify-content:space-between;align-items:center">
    <div class="wordmark" style="font-size:13px;gap:6px"><span class="mark" style="width:9px;height:9px"></span>Halvorn &amp; Vale</div>
    <div style="display:flex;gap:10px;align-items:center"><span class="btn" style="font-size:9px;padding:6px 10px">Start a Project</span><svg width="18" height="14" viewBox="0 0 18 14" stroke="#2b241e" stroke-width="1.6"><path d="M0 2h18M0 7h18M0 12h18"/></svg></div>
  </header>
  <section class="abs" style="left:14px;top:80px;width:362px;height:560px;background:linear-gradient(180deg,#f1ece4 0%,#e2d8c9 45%,#a08466 75%,#6d665c);border-radius:4px" role="img" aria-label="Slatted wood feature wall and steel stair">
    <div style="padding:22px">
      <div class="eyebrow" style="font-size:7px">Serving commercial &amp; residential clients</div>
      <h1 class="serif" style="font-size:32px;line-height:1.35;margin:8px 0 10px">Architectural Millwork Crafted Without Compromise</h1>
      <div style="display:flex;gap:10px"><span class="btn" style="font-size:10px;padding:7px 12px">Start a Project</span><span class="btn-ghost" style="font-size:10px;padding:6px 12px">Our Capabilities</span></div>
    </div>
  </section>
  <section class="abs" style="left:18px;top:670px;width:354px;height:250px">
    <div class="abs" style="left:0;top:0;width:170px"><div class="eyebrow" style="font-size:7px">About Halvorn &amp; Vale</div><h2 class="serif" style="font-size:27px;line-height:1.4;margin-top:6px">Craftsmanship Built Around Every Detail.</h2></div>
    <div class="abs" style="left:190px;top:0;width:164px"><p class="para" style="font-size:9px;line-height:1.5">Since 1988, Halvorn &amp; Vale has earned a reputation for producing architectural millwork that meets the highest standards of quality, precision, and durability. Every project is engineered, fabricated, and finished within our facility, allowing complete control from concept through installation by our skilled team.</p><span class="btn-ghost" style="font-size:9px;padding:5px 10px;margin-top:10px">Our Capabilities</span></div>
  </section>
  <div class="abs photo" style="left:14px;top:928px;width:362px;height:190px;background:linear-gradient(120deg,#8a7560,#c8b9a3 40%,#6f6354)" role="img" aria-label="Craftsmen reviewing drawings in the shop"></div>
  <section class="abs center" style="left:18px;top:1200px;width:354px">
    <div class="eyebrow" style="font-size:8px">Our Services</div>
    <h2 class="serif" style="font-size:25px;line-height:1.35;margin:6px 0 8px">From Design Intent To Final Installation</h2>
    <p class="para" style="font-size:9px">Whether fabricating reception desks, hotel millwork, boardrooms, or bespoke residential cabinetry, our team delivers exceptional craftsmanship throughout every phase.</p>
  </section>
  <section class="abs" style="left:22px;top:1420px;width:346px;display:flex;flex-direction:column;gap:22px">
    <div class="svc" style="height:185px;padding:22px"><div class="icon-box" style="width:34px;height:34px"></div><h3 style="font-size:15px;margin:14px 0 8px">Custom Architectural Millwork</h3><p style="font-size:10px">Lorem ipsum dolor sit amet, consectetur adipiscing elit, sed do eiusmod tempor incididunt ut labore et dolore magna aliqua.</p><span class="link" style="font-size:10px">Learn Our Story →</span></div>
    <div class="svc" style="height:185px;padding:22px"><div class="icon-box" style="width:34px;height:34px"></div><h3 style="font-size:15px;margin:14px 0 8px">Commercial Interiors</h3><p style="font-size:10px">Lorem ipsum dolor sit amet, consectetur adipiscing elit, sed do eiusmod tempor incididunt ut labore et dolore magna aliqua.</p><span class="link" style="font-size:10px">Learn Our Story →</span></div>
    <div class="svc" style="height:185px;padding:22px"><div class="icon-box" style="width:34px;height:34px"></div><h3 style="font-size:15px;margin:14px 0 8px">Luxury Residential Cabinetry</h3><p style="font-size:10px">Lorem ipsum dolor sit amet, consectetur adipiscing elit, sed do eiusmod tempor incididunt ut labore et dolore magna aliqua.</p><span class="link" style="font-size:10px">Learn Our Story →</span></div>
    <div class="svc" style="height:185px;padding:22px"><div class="icon-box" style="width:34px;height:34px"></div><h3 style="font-size:15px;margin:14px 0 8px">Conference Rooms</h3><p style="font-size:10px">Lorem ipsum dolor sit amet, consectetur adipiscing elit, sed do eiusmod tempor incididunt ut labore et dolore magna aliqua.</p><span class="link" style="font-size:10px">Learn Our Story →</span></div>
    <div class="svc" style="height:185px;padding:22px"><div class="icon-box" style="width:34px;height:34px"></div><h3 style="font-size:15px;margin:14px 0 8px">Educational Facilities</h3><p style="font-size:10px">Lorem ipsum dolor sit amet, consectetur adipiscing elit, sed do eiusmod tempor incididunt ut labore et dolore magna aliqua.</p><span class="link" style="font-size:10px">Learn Our Story →</span></div>
    <div class="svc" style="height:185px;padding:22px"><div class="icon-box" style="width:34px;height:34px"></div><h3 style="font-size:15px;margin:14px 0 8px">Retail Fixtures</h3><p style="font-size:10px">Lorem ipsum dolor sit amet, consectetur adipiscing elit, sed do eiusmod tempor incididunt ut labore et dolore magna aliqua.</p><span class="link" style="font-size:10px">Learn Our Story →</span></div>
  </section>
  <div class="abs center" style="left:0;right:0;top:2690px"><span class="btn" style="font-size:10px;padding:8px 16px">Start a Project</span></div>
  <section class="abs" style="left:22px;top:2760px;width:346px">
    <div class="eyebrow" style="font-size:7px">Why Choose Us</div>
    <h2 class="serif" style="font-size:24px;line-height:1.35;margin:6px 0 8px">Built To The Highest Industry Standards</h2>
    <p class="para" style="font-size:9px;width:230px">Whether fabricating reception desks, boardrooms, or residential cabinetry, our team delivers exceptional craftsmanship.</p>
    <span class="btn" style="font-size:10px;padding:7px 14px;margin-top:12px">Start a Project</span>
    <div style="display:grid;grid-template-columns:1fr 1fr;gap:12px;margin-top:26px">
      <div class="tile" style="height:110px;background:#d8cfc2;color:var(--ink);padding:12px"><h4 style="font-size:12px">36+ Years</h4></div>
      <div class="tile" style="height:110px;background:linear-gradient(135deg,#4b4540,#7a7064);padding:12px" role="img" aria-label="Finishing booth"><h4 style="font-size:12px">Premium Grade</h4></div>
      <div class="tile" style="height:110px;background:linear-gradient(135deg,#3f3a35,#6c6459);padding:12px" role="img" aria-label="Fabrication floor"><h4 style="font-size:12px">Complete Manufacturing</h4></div>
      <div class="tile" style="height:110px;background:var(--brown);padding:12px"><h4 style="font-size:12px">Award Quality</h4></div>
    </div>
  </section>
  <section class="abs" style="left:0;top:3253px;width:390px;height:1427px;background:var(--band)">
    <div class="center" style="margin-top:60px"><div class="eyebrow" style="font-size:7px">Our Portfolio</div><h2 class="serif" style="font-size:25px;margin:6px 0 8px">Showcasing Our Work</h2><p class="para" style="font-size:9px;width:320px;margin:0 auto">Explore a selection of custom millwork and cabinetry projects crafted with precision and lasting durability.</p></div>
    <div class="abs photo" style="left:50px;top:220px;width:290px;height:345px;background:linear-gradient(180deg,#2f2b28,#4a4540 55%,#6c6863)" role="img" aria-label="Executive boardroom"><div class="abs serif" style="left:16px;bottom:34px;color:#fff;font-size:16px">Executive Office Headquarters</div></div>
    <div class="abs photo" style="left:50px;top:595px;width:290px;height:345px;background:linear-gradient(180deg,#6d86a0,#9bb0c2 50%,#c9b89e)" role="img" aria-label="Blue kitchen cabinetry"></div>
    <div class="abs photo" style="left:50px;top:970px;width:290px;height:345px;background:linear-gradient(180deg,#6b4a2c,#b37a3e 45%,#9a3f23)" role="img" aria-label="Warm hospitality lounge"></div>
    <div class="abs center" style="left:0;right:0;top:1350px"><span class="btn" style="font-size:10px;padding:7px 14px">Start a Project</span></div>
  </section>
  <section class="abs" style="left:0;top:4720px;width:390px;height:520px">
    <div style="height:260px;background:linear-gradient(120deg,#7a6a4e,#c69a6a 40%,#4b6a5a 75%)" role="img" aria-label="Hospitality lounge"></div>
    <div style="height:260px;background:linear-gradient(120deg,#c6b29a,#a88c70 45%,#d9cdbd)" role="img" aria-label="Oak cabinetry interior"></div>
  </section>
  <section class="abs" style="left:18px;top:5290px;width:354px">
    <div class="photo" style="height:330px;background:linear-gradient(140deg,#6e6a66,#b3a48d 45%,#e3ddd3 70%)" role="img" aria-label="Craftsman assembling a lattice panel"></div>
    <div class="eyebrow" style="font-size:7px;margin-top:24px">Client Testimonials</div>
    <h2 class="serif" style="font-size:22px;line-height:1.35;margin:6px 0 8px">Trusted By Architects, Builders &amp; Designers</h2>
    <p class="para" style="font-size:9px">For more than three decades, Halvorn &amp; Vale has partnered with leading architects and contractors.</p>
    <div style="display:grid;grid-template-columns:1fr 1fr;gap:12px;margin-top:18px">
      <div class="quote" style="height:200px;padding:12px"><div class="stars" style="font-size:10px">★★★★★</div><p class="para" style="font-size:8px;margin-top:6px">"A beautiful and very functional kitchen. Great attention to detail throughout."</p><div style="font-size:9px;font-weight:600;margin-top:40px">Dana Merrow</div></div>
      <div class="quote" style="height:200px;padding:12px"><div class="stars" style="font-size:10px">★★★★★</div><p class="para" style="font-size:8px;margin-top:6px">"Exceptional craftsmanship and clear communication in every phase."</p><div style="font-size:9px;font-weight:600;margin-top:40px">Dana Merrow</div></div>
    </div>
  </section>
  <section class="abs" style="left:18px;top:6110px;width:354px;height:200px;background:var(--sand);padding:18px">
    <h2 class="serif" style="font-size:22px;line-height:1.35">Let's Build Something Exceptional.</h2>
    <p class="para" style="font-size:8px;margin:6px 0 10px">We'd welcome the opportunity to collaborate.</p>
    <div style="display:flex;gap:8px"><div style="flex:1;height:26px;background:#fff;border:1px solid var(--line)"></div><span class="btn" style="font-size:9px;padding:6px 12px">Contact Us</span></div>
    <div style="display:flex;gap:10px;margin-top:12px"><div style="width:22px;height:22px;border-radius:50%;background:#3e4f7a"></div><div style="width:26px;height:22px;background:#9c8a4a"></div><div style="width:22px;height:22px;border-radius:50%;background:#4f5f3c"></div></div>
  </section>
  <div class="abs photo" style="left:18px;top:6340px;width:354px;height:180px;background:linear-gradient(150deg,#3d342c,#7a6047 45%,#c2a37f 75%)" role="img" aria-label="Coffered wood ceiling interior"></div>
  <section class="abs" style="left:22px;top:6600px;width:346px">
    <div class="center"><div class="eyebrow" style="font-size:7px">Latest Insights</div><h2 class="serif" style="font-size:22px;margin:6px 0 30px">Insights &amp; Recent Projects</h2></div>
    <div style="display:flex;flex-direction:column;gap:30px">
      <div class="article" style="height:475px"><div style="height:260px;margin:12px 12px 0;background:linear-gradient(160deg,#e6ddcf,#c7a878 60%,#8d6a48)" role="img" aria-label="Bright kitchen"></div><h4>5 Architectural Millwork Trends Shaping Modern Commercial Interiors</h4><p>Discover the latest finishes and design approaches transforming offices and hospitality spaces.</p><span class="link">Read Article →</span></div>
      <div class="article" style="height:475px"><div style="height:260px;margin:12px 12px 0;background:linear-gradient(160deg,#e4e2de,#7d8fa3 55%,#564b40)" role="img" aria-label="Corporate lobby"></div><h4>Crafting a Custom Lobby for a Luxury Corporate Headquarters</h4><p>An inside look at how our team turned a vision into a sophisticated, functional space.</p><span class="link">Read Article →</span></div>
      <div class="article" style="height:475px"><div style="height:260px;margin:12px 12px 0;background:linear-gradient(160deg,#3f342b,#8c6b4a 50%,#c8b093)" role="img" aria-label="Office with wood ceiling"></div><h4>From Design to Installation: The Journey of Custom Millwork</h4><p>Follow our process from engineering and fabrication to on-site installation.</p><span class="link">Read Article →</span></div>
      <div class="article" style="height:475px"><div style="height:260px;margin:12px 12px 0;background:linear-gradient(160deg,#e1b778,#c48a48 55%,#8a5b30)" role="img" aria-label="Maple library shelving"></div><h4>Choosing the Right Wood Species for Lasting Architectural Millwork</h4><p>Compare popular hardwoods, veneers, and finishes for beauty and durability.</p><span class="link">Read Article →</span></div>
    </div>
    <div class="center" style="margin-top:24px"><span class="btn" style="font-size:10px;padding:7px 14px">Start a Project</span></div>
  </section>
  <footer class="abs" style="left:0;top:8885px;width:390px;height:655px;background:linear-gradient(180deg,#8a6849,#7b5b3f);color:#fff">
    <div style="margin-top:50px;font-family:var(--sans);font-weight:500;font-size:22px;display:flex;justify-content:center;align-items:center;gap:8px"><span style="width:12px;height:12px;background:#f2ebe2;display:inline-block"></span>Halvorn &amp; Vale</div>
    <div style="display:flex;gap:14px;justify-content:center;margin-top:20px"><div style="width:26px;height:26px;background:#f2ebe2;border-radius:4px"></div><div style="width:26px;height:26px;background:#f2ebe2;border-radius:4px"></div><div style="width:26px;height:26px;background:#f2ebe2;border-radius:4px"></div></div>
    <div style="margin:40px 22px 0"><div style="font-size:14px;font-weight:500">Contact Us</div><div style="border-bottom:1px solid #e6d8c6;padding:10px 0;font-size:10px;opacity:.85;display:flex;justify-content:space-between">Enter your email<span style="background:#f2ebe2;color:var(--brown);padding:2px 8px">Send</span></div></div>
    <div style="display:flex;gap:60px;margin:36px 22px 0">
      <div class="foot-col"><h5 style="font-size:12px">Company</h5><ul><li style="font-size:10px">Home</li><li style="font-size:10px">Projects</li><li style="font-size:10px">Services</li><li style="font-size:10px">About</li><li style="font-size:10px">Journal</li><li style="font-size:10px">Contact</li></ul></div>
      <div class="foot-col"><h5 style="font-size:12px">Contact</h5><ul><li style="font-size:10px">418 Cedar Row</li><li style="font-size:10px">Linden Falls, NC 27510</li><li style="font-size:10px">919-555-0142</li><li style="font-size:10px">studio@halvornvale.com</li></ul></div>
    </div>
    <div class="abs" style="left:22px;right:22px;bottom:40px;display:flex;justify-content:space-between;font-size:9px;opacity:.9"><span>Halvorn &amp; Vale. All Rights Reserved</span><span>Back to top ↑</span></div>
  </footer>
</main>

</body>
</html>
```